KRT Flyer - Workshop and Scholarship Program

KRT needs a double sided flyer designed for an upcoming workshop we have that is also doubling as a launch of our business and of our scholarship program.
All of the information required to go onto the flyer is contained below in the two documents.
The first is a word document that contains the details to be included on the flyer - this is in the order that I wish to present them also.
The second document is an earlier example of a winning flyer that was designed for an earlier launch. I was happy with many of the characteristics within this flyer including the photo/bio at the bottom.
Please note that the language and descriptions have all changed.
Please use images and patterns that you feel address the requirements of the advertisement.
I have included the original design files for the logo and flyer to get the logo and bio image
Target Market(s)
HSC students (Final Year of High School
Industry/Entity Type
Education
Font styles to use
Other font styles liked:
- Myriad Pro
Requirements
Must have
- The logo of the business must be shown a maximum of twice on both sides. Please remove the surrounding square and imbed it into the flyer.
- A simple but effective design
Nice to have
- Images that reflect the content
Should not have
- Too much going on that the message is lost.

```html
<!DOCTYPE html>
<html lang="en">
<head>
<meta charset="utf-8">
<title>KRT Flyer – HSC Preparation Workshop</title>
<link rel="stylesheet" href="https://fonts.googleapis.com/css2?family=Ubuntu:ital,wght@0,400;0,500;0,700;1,400;1,500&family=Open+Sans:wght@400;600;700&display=swap">
<style>
  :root {
    --navy: #1f3347;
    --navy-deep: #182a3b;
    --orange: #f47b0c;
    --orange-dark: #d8640a;
    --grey-light: #eceef0;
    --grey-mid: #c9ced3;
    --grey-cell: #dcdfe2;
    --white: #ffffff;
    --page: #dedede;
  }
  * { box-sizing: border-box; margin: 0; padding: 0; }
  html, body { width: 902px; height: 1200px; overflow: hidden; }
  body { background: var(--page); font-family: "Open Sans", Arial, sans-serif; }

  .flyer {
    position: absolute; left: 42px; top: 26px;
    width: 818px; height: 1148px;
    background: var(--white); overflow: hidden;
    box-shadow: 0 2px 10px rgba(0,0,0,.25);
  }
  .abs { position: absolute; }
  .shapes { position: absolute; left: 0; top: 0; }

  /* header */
  .headline {
    left: 42px; top: 26px; color: var(--white);
    font-family: "Ubuntu", Arial, sans-serif; font-weight: 500; line-height: 1.15;
  }
  .headline .line1 { font-size: 35px; letter-spacing: .3px; }
  .headline .line2 { font-size: 26px; }
  .headline .accent { color: var(--orange); }
  .subhead {
    left: 42px; top: 128px; color: var(--white);
    font-family: "Ubuntu", Arial, sans-serif; font-size: 19px; line-height: 1.3;
  }
  .subhead strong { font-weight: 500; }

  .brand {
    display: flex; align-items: center; gap: 8px;
    font-family: "Ubuntu", Arial, sans-serif; font-weight: 700;
    color: var(--navy); font-size: 44px; letter-spacing: 1px;
  }
  .brand-dot {
    width: 18px; height: 18px; border-radius: 50%; background: var(--orange);
  }
  .brand--top { left: 625px; top: 60px; }
  .brand--bottom { left: 545px; top: 1020px; font-size: 40px; }

  /* banner */
  .banner {
    left: 0; top: 202px; width: 818px; height: 196px;
    background: linear-gradient(180deg, #f4f5f6 0%, #e7e9eb 100%);
    border-bottom: 3px solid var(--orange);
  }
  .student-photo { background: linear-gradient(180deg, #d7c2b4, #b9584a); border-radius: 4px; }
  .student-photo--left { left: 82px; top: 12px; width: 86px; height: 180px; }
  .student-photo--right { left: 640px; top: 12px; width: 100px; height: 180px;
    background: linear-gradient(180deg, #c9a68c, #a24a6a); }
  .banner-title {
    left: 0; width: 818px; top: 20px; text-align: center;
    font-family: "Ubuntu", Arial, sans-serif; color: var(--navy);
  }
  .banner-title .big { color: var(--orange); font-size: 76px; font-weight: 500; line-height: 1; display: block; letter-spacing: 1px; }
  .banner-title .sub { font-size: 27px; font-weight: 500; line-height: 1.3; display: block; margin-top: 6px; }

  /* content */
  .agenda {
    left: 0; top: 401px; width: 818px; height: 324px;
    background: var(--navy);
  }
  .agenda-photo {
    left: 385px; top: 0; width: 433px; height: 324px;
    background: linear-gradient(90deg, rgba(31,51,71,1) 0%, #6f7e8c 28%, #b7a695 60%, #d9c7b2 100%);
  }
  .agenda-tab {
    left: 0; top: 9px; height: 31px; width: 292px;
    background: var(--orange); color: var(--white);
    font-family: "Ubuntu", Arial, sans-serif; font-size: 18px;
    padding: 4px 0 0 40px;
    clip-path: polygon(0 0, 100% 0, 91% 100%, 0 100%);
  }
  .agenda-list { left: 40px; top: 56px; width: 360px; list-style: none; color: var(--white); font-size: 11.4px; line-height: 1.3; }
  .agenda-list > li { position: relative; padding-left: 16px; margin-bottom: 6.5px; }
  .agenda-list > li::before {
    content: ""; position: absolute; left: 0; top: 4px;
    width: 7px; height: 7px; border-radius: 50%; background: var(--orange);
  }
  .sub-list { list-style: none; margin-top: 8px; }
  .sub-list li { position: relative; padding-left: 40px; margin-bottom: 7px; }
  .sub-list svg { position: absolute; left: 22px; top: 2px; }

  /* sessions table */
  .sessions {
    left: 40px; top: 741px; width: 745px; height: 211px;
    display: flex; gap: 4px;
    border-radius: 12px; overflow: hidden;
    box-shadow: 0 3px 8px rgba(0,0,0,.35);
    background: var(--white);
  }
  .session { flex: 1; display: flex; flex-direction: column; }
  .session-head {
    height: 38px; background: var(--orange); color: var(--white);
    font-weight: 700; font-size: 13.5px; text-align: center; line-height: 38px;
    border-bottom: 2px solid var(--navy);
  }
  .row { display: flex; font-size: 11.5px; }
  .row .label { width: 94px; padding-left: 18px; font-weight: 600; color: var(--navy); letter-spacing: .3px; background: var(--grey-cell); }
  .row .value { flex: 1; padding-left: 18px; font-weight: 700; color: var(--navy); background: var(--grey-light); }
  .row--date { height: 66px; }
  .row--date .label, .row--date .value { padding-top: 14px; line-height: 26px; }
  .row--time { height: 44px; }
  .row--time .label { background: var(--grey-mid); padding-top: 12px; }
  .row--time .value { background: var(--grey-mid); padding-top: 8px; line-height: 1.25; }
  .row--cost { flex: 1; }
  .row--cost .label { padding-top: 20px; }
  .row--cost .value { background: var(--white); padding-top: 10px; line-height: 1.3; }

  /* registration */
  .register-tab {
    left: 0; top: 995px; width: 230px; height: 32px;
    background: var(--orange); color: var(--white);
    font-family: "Ubuntu", Arial, sans-serif; font-size: 18px; font-weight: 500;
    padding: 4px 0 0 40px;
    clip-path: polygon(0 0, 100% 0, 88% 100%, 0 100%);
  }
  .register-text {
    left: 42px; top: 1038px; width: 340px; color: var(--white);
    font-family: "Ubuntu", Arial, sans-serif; font-style: italic; font-size: 12.5px; line-height: 1.4;
  }
  .register-text .phone-line { font-style: normal; font-weight: 700; font-size: 22px; display: block; margin-bottom: 2px; }
  .register-text .phone-line span { color: var(--orange); }
  .turn-over {
    left: 428px; top: 1092px; width: 370px; color: var(--white);
    font-family: "Ubuntu", Arial, sans-serif; font-size: 12.5px; font-weight: 500; line-height: 1.3;
  }
</style>
</head>
<body>
<main class="flyer">
  <svg class="shapes" width="818" height="1148" viewBox="0 0 818 1148" aria-hidden="true">
    <!-- header blocks -->
    <rect x="527" y="0" width="291" height="22" fill="#f47b0c"/>
    <polygon points="0,0 600,0 526,117 0,117" fill="#1f3347"/>
    <polygon points="0,122 474,122 417,182 0,182" fill="#f47b0c"/>
    <polygon points="474,122 417,182 440,182" fill="#d8640a"/>
    <rect x="0" y="190" width="818" height="8" fill="#1f3347"/>
    <!-- bottom blocks -->
    <polygon points="0,1016 403,1016 430,1082 403,1082 403,1148 0,1148" fill="#182a3b"/>
    <rect x="403" y="1082" width="415" height="66" fill="#f47b0c"/>
  </svg>

  <div class="abs headline">
    <div class="line1">LIMITED SPOTS AVAILABLE</div>
    <div class="line2">AT BOTH VENUES! <span class="accent">DON’T MISS OUT!</span></div>
  </div>
  <div class="abs subhead">This event could make all the difference<br><strong>to your HSC Experience!</strong></div>
  <div class="abs brand brand--top"><span class="brand-dot"></span>KRT</div>

  <section class="abs banner">
    <div class="abs student-photo student-photo--left" role="img" aria-label="Smiling female student peeking from behind the banner"></div>
    <div class="abs student-photo student-photo--right" role="img" aria-label="Smiling male student peeking from behind the banner"></div>
    <h1 class="abs banner-title">
      <span class="big">2017 FREE</span>
      <span class="sub">HSC PREPARATION WORKSHOP<br>AND SCHOLARSHIP OFFER</span>
    </h1>
  </section>

  <section class="abs agenda">
    <div class="abs agenda-photo" role="img" aria-label="Group of happy graduating students, one in a mortar board holding a diploma"></div>
    <h2 class="abs agenda-tab">What will the day involve?</h2>
    <ul class="abs agenda-list">
      <li>Establishing individual goals for the year ahead</li>
      <li>Developing the right mindset for the HSC</li>
      <li>Participating in case studies that simulate the Year 12 experience</li>
      <li>Understanding the importance of starting early and keeping up to date</li>
      <li>Learning about the importance of maintaining notes</li>
      <li>Strategies to increase the EFFICIENCY AND EFFECTIVENESS of your studies while decreasing levels of PROCRASTINATION</li>
      <li>Planning a BALANCED approach to studies and AVOIDING BURNOUT with:
        <ul class="sub-list">
          <li><svg width="11" height="10" viewBox="0 0 11 10"><path d="M1 5 L4 8 L10 1" fill="none" stroke="#f47b0c" stroke-width="2"/></svg>The 4 stages of examination preparation</li>
          <li><svg width="11" height="10" viewBox="0 0 11 10"><path d="M1 5 L4 8 L10 1" fill="none" stroke="#f47b0c" stroke-width="2"/></svg>The 7 habits of highly effective students</li>
          <li><svg width="11" height="10" viewBox="0 0 11 10"><path d="M1 5 L4 8 L10 1" fill="none" stroke="#f47b0c" stroke-width="2"/></svg>The 8 steps to Academic Success</li>
        </ul>
      </li>
    </ul>
  </section>

  <section class="abs sessions">
    <div class="session">
      <div class="session-head">PRESENTATION 1</div>
      <div class="row row--date"><div class="label">DATE<br>LOCATION</div><div class="value">Monday 3rd October, 2016<br>Penrith</div></div>
      <div class="row row--time"><div class="label">TIME</div><div class="value">Session 1 – 10:00– 1:00(20 seats available)<br>Session 2 – 2:00 – 5:00(20 seats available)</div></div>
      <div class="row row--cost"><div class="label">COST</div><div class="value">FREE*<br>Secure your spot with a $20 deposit that is returned at the end of the presentation</div></div>
    </div>
    <div class="session">
      <div class="session-head">PRESENTATION 2</div>
      <div class="row row--date"><div class="label">DATE<br>LOCATION</div><div class="value">Tuesday 4th October, 2016<br>Burwood</div></div>
      <div class="row row--time"><div class="label">TIME</div><div class="value">Session 1 – 10:00– 1:00(20 seats available)<br>Session 2 – 2:00 – 5:00(20 seats available)</div></div>
      <div class="row row--cost"><div class="label">COST</div><div class="value">FREE*<br>Secure your spot with a $20 deposit that is returned at the end of the presentation</div></div>
    </div>
  </section>

  <h2 class="abs register-tab">How to register:</h2>
  <p class="abs register-text">
    <span class="phone-line">Text <span>0400 555 123</span></span>
    with your name, email address and the session date and time you wish to attend. An email will then be sent confirming further details.
  </p>
  <div class="abs brand brand--bottom"><span class="brand-dot"></span>KRT</div>
  <p class="abs turn-over">Turn over to read about the inaugural Keystone Results Training Scholarship Program</p>
</main>
</body>
</html>
```